Summer Sale Graphics for Social Media

I want to create 11 social media graphics (new Instagram size 4:5 (1080 x 1350 pixels) focusing on our Summer Sale Graphics, using any of the pics attached. Use the attached pics, NO RANDOM STOCK PHOTOGRAPHY. For the color scheme of the graphics, they should all be complementary to the product colors in the photos.
You can add any of the photos attached but none are required. You can do some of the graphics in all text. I mainly need BOLD text that says one of the headlines (11 total) SEE ATTACHED WORD DOCUMENT for the headlines to use.

```html
<!DOCTYPE html>
<html lang="en">
<head>
<meta charset="utf-8">
<title>Summer Sale Social Graphics</title>
<link rel="stylesheet" href="https://fonts.googleapis.com/css2?family=Great+Vibes&family=Montserrat:wght@400;500;600;700;800;900&family=Oswald:wght@300;400;500;600;700&display=swap">
<style>
:root{
  --board:#e4e4e4;
  --card:#ffffff;
  --ink:#111111;
  --red:#ee2b2b;
  --brown:#8b5a3c;
  --green:#2f5a4b;
  --purple:#4a3f8a;
  --magenta:#d4006b;
  --band-a:#ee2b2b;
  --band-b:#fbd3d3;
  --photo-light:#f1efee;
  --photo-mid:#c9b2a2;
  --photo-dark:#3a2a24;
}
*{margin:0;padding:0;box-sizing:border-box}
html,body{width:1200px;height:992px;overflow:hidden;background:var(--board)}
.board{position:relative;width:1200px;height:992px}
.post{position:absolute;width:182px;height:236px;background:var(--card);box-shadow:0 2px 6px rgba(0,0,0,.18);overflow:hidden;color:var(--ink)}
.post--framed{border:1px solid #333}
.line{position:absolute;left:0;right:0;text-align:center;line-height:1;white-space:nowrap}
.line--left{left:7px;right:auto;text-align:left}
.script{font-family:"Great Vibes",cursive;font-weight:400}
.cond{font-family:"Oswald",sans-serif}
.sans{font-family:"Montserrat",sans-serif}
.photo{position:absolute;background:linear-gradient(180deg,var(--photo-light) 0%,var(--photo-mid) 45%,var(--photo-dark) 100%)}
.offer-band{position:absolute;left:0;right:0;top:212px;height:12px;background:linear-gradient(90deg,var(--band-b),var(--band-a) 15%,var(--band-a) 85%,var(--band-b));color:#fff;font:600 8px/12px "Montserrat",sans-serif;text-align:center;letter-spacing:.5px}
.rule{display:inline-block;width:30px;height:3px;background:var(--ink);vertical-align:middle;margin:0 4px}
.c-red{color:var(--red)}.c-brown{color:var(--brown)}.c-green{color:var(--green)}
.c-purple{color:var(--purple)}.c-mag{color:var(--magenta)}.c-gray{color:#555}
</style>
</head>
<body>
<main class="board">

  <section class="post" style="left:88px;top:76px">
    <p class="line script" style="top:8px;font-size:30px">Your</p>
    <p class="line cond c-red" style="top:44px;font-size:24px;font-weight:600">SUMMER BODY</p>
    <p class="line cond" style="top:80px;font-size:19px">WON'T WAIT</p>
    <p class="line sans c-red" style="top:110px;font-size:42px;font-weight:600">SALE</p>
    <p class="line sans c-red" style="top:156px;font-size:42px;font-weight:600">NOW!</p>
    <p class="offer-band">Upto $15 OFF</p>
  </section>

  <section class="post" style="left:280px;top:74px;height:226px">
    <div class="photo" style="left:100px;top:20px;width:81px;height:190px" role="img" aria-label="Woman holding supplement bottles"></div>
    <p class="line line--left cond c-brown" style="top:4px;font-size:32px;font-weight:700">DETOX,</p>
    <p class="line line--left cond c-brown" style="top:40px;font-size:32px;font-weight:700">BURN FAT,</p>
    <p class="line line--left sans" style="top:84px;font-size:10px">&amp;</p>
    <p class="line line--left cond c-brown" style="top:96px;font-size:18px;font-weight:600">Turn Heads</p>
    <p class="line line--left cond c-gray" style="top:118px;font-size:18px;font-weight:300">THIS SUMMER</p>
    <p class="line line--left sans" style="top:140px;font-size:27px;font-weight:600">SALE</p>
    <p class="line line--left sans" style="top:170px;font-size:27px;font-weight:600">NOW!</p>
    <p class="offer-band" style="top:202px">Upto $15 OFF</p>
  </section>

  <section class="post" style="left:493px;top:73px;height:227px">
    <p class="line cond c-green" style="top:24px;font-size:28px;font-weight:600">One Sale</p>
    <p class="line cond c-green" style="top:64px;font-size:28px;font-weight:600">One Body</p>
    <p class="line cond c-green" style="top:105px;font-size:28px;font-weight:600">One Summer</p>
    <p class="line cond c-green" style="top:146px;font-size:28px;font-weight:600">to Slay</p>
    <p class="offer-band" style="top:211px">Upto $15 OFF</p>
  </section>

  <section class="post" style="left:708px;top:73px;height:235px">
    <div class="photo" style="left:94px;top:20px;width:88px;height:190px" role="img" aria-label="Woman with row of supplement bottles"></div>
    <p class="line line--left script" style="top:6px;font-size:22px">Hurry!</p>
    <p class="line line--left sans c-red" style="top:36px;font-size:28px;font-weight:900">OUR</p>
    <p class="line line--left sans c-red" style="top:68px;font-size:20px;font-weight:900">SUMMER</p>
    <p class="line line--left sans" style="top:94px;font-size:13px;font-weight:500">Slim-Down</p>
    <p class="line line--left sans c-red" style="top:110px;font-size:13px;font-weight:800">SALE IS ON</p>
    <p class="line line--left sans" style="top:136px;font-size:22px;font-weight:700">Don't</p>
    <p class="line line--left sans" style="top:164px;font-size:15px;font-weight:600">Miss It!</p>
    <p class="offer-band">Upto $15 OFF</p>
  </section>

  <section class="post" style="left:918px;top:67px">
    <div class="photo" style="left:92px;top:40px;width:90px;height:196px" role="img" aria-label="Woman with supplement bottles on table"></div>
    <p class="line cond" style="top:0;font-size:40px;font-weight:700">SALE</p>
    <p class="line cond c-red" style="top:44px;font-size:26px;font-weight:700">YOUR SUMMER</p>
    <p class="line line--left cond" style="top:82px;font-size:28px;font-weight:700">BODY</p>
    <p class="line line--left cond" style="top:112px;font-size:28px;font-weight:700">STARTS</p>
    <p class="line line--left cond" style="top:142px;font-size:28px;font-weight:700">HERE</p>
  </section>

  <section class="post" style="left:90px;top:332px;height:235px">
    <p class="line script" style="top:8px;font-size:26px">Final</p>
    <p class="line cond c-purple" style="top:40px;font-size:24px;font-weight:700">COUNTDOWN</p>
    <p class="line cond" style="top:72px;font-size:22px">TO SUMMER</p>
    <p class="line sans c-purple" style="top:110px;font-size:42px;font-weight:600">SALE</p>
    <p class="line sans c-purple" style="top:156px;font-size:42px;font-weight:600">NOW!</p>
    <p class="offer-band">Upto $15 OFF</p>
  </section>

  <section class="post" style="left:286px;top:335px;height:235px">
    <div class="photo" style="left:92px;top:0;width:90px;height:210px" role="img" aria-label="Woman with supplement bottles on table"></div>
    <p class="line line--left cond c-red" style="top:8px;font-size:24px;font-weight:700">SUMMER'S</p>
    <p class="line line--left cond c-red" style="top:36px;font-size:38px;font-weight:700">HERE</p>
    <p class="line line--left sans" style="top:88px;font-size:10px">And We're</p>
    <p class="line line--left sans" style="top:101px;font-size:10px">Having the</p>
    <p class="line line--left cond c-red" style="top:116px;font-size:20px;font-weight:700">BIGGEST</p>
    <p class="line line--left cond c-red" style="top:138px;font-size:34px;font-weight:700">SALE</p>
    <p class="line line--left sans" style="top:182px;font-size:12px">of the Year</p>
    <p class="offer-band">Upto $15 OFF</p>
  </section>

  <section class="post" style="left:482px;top:342px;height:235px">
    <p class="line sans c-mag" style="top:8px;font-size:28px;font-weight:900">SUMMER</p>
    <p class="line sans" style="top:42px;font-size:9px;font-weight:500"><span class="rule"></span>Isn't Waiting -<span class="rule"></span></p>
    <p class="line sans c-mag" style="top:56px;font-size:28px;font-weight:900">NEITHER</p>
    <p class="line sans c-mag" style="top:92px;font-size:16px;font-weight:900">SHOULD YOU</p>
    <p class="line sans c-mag" style="top:116px;font-size:38px;font-weight:600">SALE</p>
    <p class="line sans c-mag" style="top:160px;font-size:38px;font-weight:600">NOW!</p>
    <p class="offer-band">Upto $15 OFF</p>
  </section>

  <section class="post" style="left:695px;top:348px">
    <div class="photo" style="left:100px;top:20px;width:82px;height:192px" role="img" aria-label="Woman holding supplement bottles"></div>
    <p class="line line--left sans" style="top:6px;font-size:24px;font-weight:500">SLIM</p>
    <p class="line line--left sans c-purple" style="top:34px;font-size:26px;font-weight:900">WAIST</p>
    <p class="line line--left sans" style="top:64px;font-size:24px;font-weight:500">FLAT</p>
    <p class="line line--left sans c-purple" style="top:94px;font-size:18px;font-weight:900">TUMMY</p>
    <p class="line line--left sans" style="top:116px;font-size:9px;font-weight:800">MORE ENERGY.</p>
    <p class="line line--left script" style="top:128px;font-size:17px">Let's Go!</p>
    <p class="line line--left sans c-purple" style="top:148px;font-size:28px;font-weight:600">SALE</p>
    <p class="line line--left sans c-purple" style="top:180px;font-size:28px;font-weight:600">NOW!</p>
    <p class="offer-band">Upto $15 OFF</p>
  </section>

  <section class="post post--framed" style="left:919px;top:359px">
    <div class="photo" style="left:96px;top:10px;width:84px;height:200px" role="img" aria-label="Woman with supplement bottles on table"></div>
    <p class="line line--left cond" style="top:8px;font-size:15px;font-weight:700">Limited-Time</p>
    <p class="line line--left sans c-mag" style="top:34px;font-size:22px;font-weight:700">SUMMER</p>
    <p class="line line--left sans c-mag" style="top:58px;font-size:32px;font-weight:900">SALE</p>
    <p class="line line--left sans" style="top:96px;font-size:22px;font-weight:600">Snatch</p>
    <p class="line line--left sans" style="top:120px;font-size:22px;font-weight:600">Your</p>
    <p class="line line--left sans c-mag" style="top:148px;font-size:14px;font-weight:800">Supplements</p>
    <p class="line line--left sans" style="top:168px;font-size:13px;font-weight:600">Now!</p>
    <p class="offer-band">Upto $15 OFF</p>
  </section>

  <section class="post" style="left:479px;top:610px">
    <p class="line script" style="top:10px;font-size:26px">Get Snatched</p>
    <p class="line sans c-mag" style="top:50px;font-size:17px;font-weight:900">FOR SUMMER -</p>
    <p class="line sans c-mag" style="top:74px;font-size:17px;font-weight:900">SUPPLEMENTS</p>
    <p class="line sans" style="top:100px;font-size:16px;font-weight:500">ON</p>
    <p class="line sans c-mag" style="top:120px;font-size:40px;font-weight:900">SALE</p>
    <p class="line sans c-mag" style="top:164px;font-size:40px;font-weight:900">NOW!</p>
    <p class="offer-band">Upto $15 OFF</p>
  </section>

</main>
</body>
</html>
```